New Modern Wix Website Design

We are NOT your typical electrical/home improvement contractor, so we need our website updated. We already have a logo for each division.
We provided a neutral logo with a hard hat, a logo for the home improvement, and a logo for the electrical division. (if we can implement all 3 logos will be great but at least the 2 for the divisions must be used.

We looking for a website that a 10-year-old can understand, our target audience is the new young generation that wants innovations in their properties, smart homes, cool smart things/gadgets. So we need a website that is fun, simple, eye-catching. (we don't want to appear TOO serious and boring)
NO GENERIC WEBSITES SO MUST BE VERY CREATIVE!!!

We want to be able to share google reviews, a contact box, business hours, our services, etc...

current website sirvantelo.us

Target Market(s)

Contractors in different trades.

Industry/Entity Type

Construction

Colors
FFC000
F8CF3A
FAE287
FDF2CF
FEFAEE

Requirements
Must have
• Modern upmarket look and feel
Nice to have
• already attached supporting images.
Should not have
• basic typical construction boring and depressing look and feel.

```html
<!DOCTYPE html>
<html lang="en">
<head>
<meta charset="utf-8">
<title>Sir Vantelo — Home</title>
<link href="https://fonts.googleapis.com/css2?family=Anton&family=Roboto:ital,wght@0,400;0,500;0,700;1,400&display=swap" rel="stylesheet">
<style>
:root{
  --gold:#b8862a;
  --gold-light:#d4a55a;
  --ink:#111111;
  --dark:#1b1b1b;
  --footer:#2b2b2b;
  --text:#555555;
  --muted:#8a8a8a;
  --paper:#ffffff;
  --mist:#f2f2f2;
  --line:#dddddd;
}
*{margin:0;padding:0;box-sizing:border-box}
html,body{width:1200px;height:4409px;overflow:hidden;background:var(--paper)}
body{position:relative;font-family:"Roboto",Arial,sans-serif;color:var(--text)}
.abs{position:absolute}
.display{font-family:"Anton",Impact,sans-serif;font-weight:400;color:var(--ink);letter-spacing:.5px}
.btn{position:absolute;display:flex;align-items:center;gap:10px;justify-content:center;background:var(--gold);color:#fff;font:700 14px "Roboto",Arial,sans-serif;text-transform:uppercase;border-radius:2px}
.btn .dot{width:13px;height:13px;border-radius:50%;background:#fff;position:relative}
.btn .dot::after{content:"";position:absolute;left:4px;top:3.5px;border-left:6px solid var(--gold);border-top:3px solid transparent;border-bottom:3px solid transparent}
.brand-name{font-family:"Anton",Impact,sans-serif;color:var(--ink);letter-spacing:1px;white-space:nowrap}

/* header */
.site-header{position:absolute;left:0;top:0;width:1200px;height:123px;background:#fff}
.contact-chip{position:absolute;top:14px;display:flex;align-items:center;gap:12px;font-size:15px;color:#555}
.chip-icon{width:28px;height:28px;border-radius:50%;background:var(--gold);display:flex;align-items:center;justify-content:center}
.nav{position:absolute;top:80px;display:flex;gap:28px;font:500 13.5px "Roboto",Arial,sans-serif;color:#111;text-transform:uppercase}
.header-rule{position:absolute;top:60px;height:1px;background:var(--line)}
.logo-tab{position:absolute;left:493px;top:0;width:214px;height:149px;background:#fff;border-radius:0 0 30px 30px;z-index:3;display:flex;flex-direction:column;align-items:center;justify-content:center;gap:6px}
.logo-tab .mark{width:26px;height:26px;border-radius:50%;background:var(--gold)}
.social{position:absolute;top:12px;width:30px;height:30px;border-radius:50%;background:var(--gold)}
.login{position:absolute;left:1036px;top:16px;font:500 17px "Roboto",Arial,sans-serif;color:var(--gold);display:flex;gap:8px;align-items:center}

/* hero */
.hero{position:absolute;left:0;top:123px;width:1200px;height:742px}
.hero-photo{position:absolute;inset:0;height:700px;background:linear-gradient(180deg,#8b8478 0%,#a79c88 35%,#c7b37a 65%,#6b5d45 100%);clip-path:polygon(0 0,100% 0,100% 519px,50% 682px,0 519px)}
.hero h1{position:absolute;top:100px;width:100%;text-align:center;font-size:66px;color:#fff}
.hero p{position:absolute;top:196px;left:330px;width:540px;text-align:center;color:#fff;font:500 15px/27px "Roboto",Arial,sans-serif}

/* about */
.about-mark{position:absolute;left:185px;top:940px;width:320px;height:580px;display:flex;flex-direction:column;align-items:center;justify-content:center;gap:24px}
.about-mark .mark{width:90px;height:90px;border-radius:50%;background:var(--gold)}
.about-mark .brand-name{font-size:58px}
.about h2{position:absolute;left:642px;top:1000px;font-size:50px}
.about p{position:absolute;left:642px;width:445px;font-size:15.5px;line-height:27.5px;color:#666}

/* split */
.split{position:absolute;left:0;top:1618px;width:1200px;height:560px}
.division{position:absolute;top:112px;width:440px;text-align:center;color:#fff}
.division .brand-name{color:#fff;font-size:22px;display:flex;align-items:center;justify-content:center;gap:8px}
.division .brand-name i{width:14px;height:14px;border-radius:50%;background:#fff;display:inline-block}
.division p{margin-top:20px;font-size:14.5px;line-height:26px}
.division .more{margin-top:20px;display:inline-flex;gap:8px;align-items:center;font:500 12.5px "Roboto",Arial,sans-serif;text-transform:uppercase}
.division .more .dot{width:12px;height:12px;border-radius:50%;background:#fff}

/* quality */
.quality h2{position:absolute;left:111px;top:2210px;font-size:38px}
.quality p{position:absolute;left:111px;width:470px;font-size:14px;line-height:26px;color:#666}
.quality-frame{position:absolute;left:630px;top:2405px;width:570px;height:210px;border:4px solid var(--gold);border-right:none}
.quality-photo{position:absolute;left:652px;top:2220px;width:548px;height:368px;background:linear-gradient(135deg,#8a8f96,#c9ccd0 45%,#7b2f2a 60%,#5d636b)}

/* newsletter */
.newsletter{position:absolute;left:0;top:2725px;width:1200px;height:189px;background:linear-gradient(90deg,#a87a32,#d5b072 45%,#c39a55 70%,#9c722c)}
.newsletter h3{position:absolute;left:113px;top:26px;font-size:36px;color:#fff}
.newsletter p{position:absolute;left:115px;top:84px;width:360px;color:#fff;font-size:15px;line-height:24px}
.news-form{position:absolute;left:533px;top:70px;width:553px;height:50px;background:#fff;display:flex;align-items:center}
.news-form span{flex:1;padding-left:48px;font-size:14px;color:#888;position:relative}
.news-form span::before{content:"";position:absolute;left:22px;top:3px;width:14px;height:10px;background:#777;border-radius:1px}
.news-form b{width:152px;height:100%;background:var(--gold);color:#fff;font:700 14px "Roboto",Arial,sans-serif;display:flex;align-items:center;justify-content:center;border:2px solid #fff}

/* testimonials */
.testimonials h2{position:absolute;top:3005px;width:1200px;text-align:center;font-size:38px}
.quote-card{position:absolute;top:3087px;width:320px;height:209px;background:#fff;box-shadow:0 0 10px rgba(0,0,0,.1)}
.quote-card.featured{background:#000}
.quote-card .flag{position:absolute;left:0;top:0;width:0;height:0;border-top:46px solid var(--gold);border-right:46px solid transparent}
.quote-card .flag i{position:absolute;left:6px;top:-42px;color:#fff;font:700 16px "Anton",Impact,sans-serif}
.quote-card p{position:absolute;left:29px;top:42px;width:275px;font:italic 13px/23px "Roboto",Arial,sans-serif;color:#888}
.quote-card.featured p{color:#fff}
.stars{position:absolute;left:29px;top:122px;color:#f5c518;font-size:13px;letter-spacing:2px}
.avatar{position:absolute;left:29px;top:148px;width:58px;height:46px;background:linear-gradient(135deg,#d8d8d8,#9aa2ab)}
.who{position:absolute;left:113px;top:152px;font-size:13px;line-height:17px;color:#222}
.who b{display:block;font-weight:500}
.featured .who{color:#fff}

/* contact */
.contact{position:absolute;left:0;top:3390px;width:1200px;height:590px;background:var(--mist)}
.machines{position:absolute;left:0;top:3790px;width:1200px;height:190px;background:linear-gradient(180deg,rgba(200,200,200,0),#d9d9d9)}
.contact-panel{position:absolute;left:147px;top:3472px;width:363px;height:303px;background:var(--gold)}
.contact-panel small{position:absolute;right:115px;top:58px;font:400 14px "Anton",Impact,sans-serif;color:#fff;letter-spacing:.5px}
.contact-panel small::after{content:"";position:absolute;right:-15px;top:3px;width:4px;height:14px;background:#fff}
.contact-panel h3{position:absolute;right:110px;top:98px;text-align:right;font:400 46px/56px "Anton",Impact,sans-serif;color:#fff}
.contact-frame{position:absolute;left:767px;top:3472px;width:294px;height:303px;border:4px solid var(--gold)}
.form-card{position:absolute;left:443px;top:3510px;width:572px;height:390px;background:#fff}
.form-card h4{position:absolute;left:42px;top:36px;font-size:27px}
.field{position:absolute;width:230px;border-bottom:1px solid var(--line);padding-bottom:8px}
.field label{display:block;font:700 13px "Roboto",Arial,sans-serif;color:#222;margin-bottom:16px}
.field span{font-size:11px;color:#888}
.send{position:absolute;left:482px;top:312px;width:50px;height:50px;border-radius:50%;background:var(--gold)}

/* footer */
.site-footer{position:absolute;left:0;top:3980px;width:1200px;height:429px;background:var(--footer);color:#fff}
.footer-brand{position:absolute;left:150px;top:80px;width:180px;height:220px;display:flex;flex-direction:column;align-items:center;justify-content:center;gap:14px}
.footer-brand .mark{width:54px;height:54px;border-radius:50%;background:#fff}
.footer-brand .brand-name{color:#fff;font-size:30px}
.f-col{position:absolute;top:107px}
.f-col h5{font:500 17px "Roboto",Arial,sans-serif}
.f-col h5::after{content:"";display:block;width:30px;height:2px;background:#fff;margin-top:10px}
.f-col ul{list-style:none;margin-top:20px}
.f-col li{font-size:13.5px;line-height:31px;padding-left:24px;position:relative}
.f-col li::before{content:"»";position:absolute;left:0;color:var(--gold)}
.f-contact div{font-size:13.5px;line-height:20px;padding-left:37px;position:relative;margin-bottom:18px}
.f-contact i{position:absolute;left:2px;top:3px;width:12px;height:12px;background:var(--gold);border-radius:50%}
.footer-bottom{position:absolute;top:4371px;font-size:13.5px;color:#fff}
</style>
</head>
<body>

<header class="site-header">
  <div class="contact-chip" style="left:90px">
    <span class="chip-icon"><svg width="13" height="10" viewBox="0 0 13 10"><rect x="0.5" y="0.5" width="12" height="9" fill="none" stroke="#fff"/><path d="M0.5 0.5 L6.5 5.5 L12.5 0.5" fill="none" stroke="#fff"/></svg></span>info@sirvantelo.us
  </div>
  <div class="contact-chip" style="left:287px">
    <span class="chip-icon"><svg width="13" height="13" viewBox="0 0 24 24"><path fill="#fff" d="M6.6 10.8a15.1 15.1 0 006.6 6.6l2.2-2.2a1 1 0 011-.25 11.4 11.4 0 003.6.57 1 1 0 011 1V20a1 1 0 01-1 1A17 17 0 013 4a1 1 0 011-1h3.5a1 1 0 011 1c0 1.25.2 2.45.57 3.57a1 1 0 01-.25 1z"/></svg></span>+1 (555) 240-1187
  </div>
  <div class="header-rule" style="left:90px;width:390px"></div>
  <div class="header-rule" style="left:745px;width:368px"></div>
  <nav class="nav" style="left:90px"><span>Home</span><span>About Us</span><span>Job Opportunities</span></nav>
  <nav class="nav" style="left:821px"><span>About</span><span>What We Offer</span><span>Contact Us</span></nav>
  <span class="social" style="left:826px"></span>
  <span class="social" style="left:864px"></span>
  <div class="login"><svg width="14" height="14" viewBox="0 0 14 14"><circle cx="7" cy="4" r="3.2" fill="#b8862a"/><path d="M1 14c0-4 2.7-5.5 6-5.5s6 1.5 6 5.5z" fill="#b8862a"/></svg>LOG IN</div>
  <div class="logo-tab"><span class="mark"></span><span class="brand-name" style="font-size:30px">SIR VANTELO</span></div>
</header>

<section class="hero">
  <svg class="abs" style="left:0;top:0" width="1200" height="742" viewBox="0 0 1200 742"><polygon points="0,505 600,668 1200,505 1200,530 600,742 0,530" fill="#b8862a"/></svg>
  <div class="hero-photo" role="img" aria-label="Two builders in hard hats and safety vests on a construction site"></div>
  <h1 class="display">SIR VANTELO</h1>
  <p>We founded Sir Vantelo out of a pure passion for people. Our goals, our ambitions, our inspirations, all come together</p>
  <div class="btn" style="left:519px;top:275px;width:162px;height:50px">Get Started <span class="dot"></span></div>
</section>

<section class="about">
  <div class="about-mark"><span class="mark"></span><span class="brand-name">SIR VANTELO</span></div>
  <h2 class="display">ABOUT US</h2>
  <p style="top:1085px">We founded Sir Vantelo out of a pure passion for people. Our goals, our ambitions, our inspirations, all come together to form a truly amazing company that all of us are proud to be a part of.</p>
  <p style="top:1222px">Since opening back in 2016, we have become masters at our craft. We go above and beyond your requests to keep you coming back for more. Explore the rest of our site to learn more about what we offer, and get in touch with any questions.</p>
  <div class="btn" style="left:642px;top:1396px;width:163px;height:50px">Learn More <span class="dot"></span></div>
</section>

<section class="split">
  <svg class="abs" style="left:0;top:0" width="1200" height="560" viewBox="0 0 1200 560"><polygon points="0,0 700,130 700,430 0,560" fill="#b8862a"/><polygon points="548,118 1200,0 1200,560 548,494" fill="#1b1b1b"/></svg>
  <div class="division" style="left:80px">
    <div class="brand-name"><i></i>SIR VANTELO</div>
    <p>Lorem ipsum dolor sit amet, consectetur adipiscing elit, sed do eiusmod tempor incididunt ut labore et dolore magna aliqua. Ut enim ad minim veniam, quis noexercitation ullamco laboris nisi ut aliquip ex ea commodo cons equat. Duis aute irure dolor in reprehenderit in voluptate velit esse cillum dolore eu fugiat nulla pariatur. Excepteur sint occaecat cupidatat non proident,</p>
    <div class="more">Learn More <span class="dot"></span></div>
  </div>
  <div class="division" style="left:654px">
    <div class="brand-name"><i></i>SIR VANTELO</div>
    <p>Lorem ipsum dolor sit amet, consectetur adipiscing elit, sed do eiusmod tempor incididunt ut labore et dolore magna aliqua. Ut enim ad minim veniam, quis noexercitation ullamco laboris nisi ut aliquip ex ea commodo cons equat. Duis aute irure dolor in reprehenderit in voluptate velit esse cillum dolore eu fugiat nulla pariatur. Excepteur sint occaecat cupidatat non proident,</p>
    <div class="more">Learn More <span class="dot"></span></div>
  </div>
</section>

<section class="quality">
  <h2 class="display">QUALITY &amp; INTEGRITY</h2>
  <p style="top:2284px">Sir Vantelo is completely dedicated to client satisfaction. All of our team members are punctual and knowledgeable, helping make us some of the most trusted contractors in the industry. We've come a long way since our founding in 2016, but the leading operating values behind our services, to work with integrity in order to provide high-quality services to our clients, remain unchanged.</p>
  <p style="top:2466px">Please get in touch with any inquiries. Be sure to include your contact information as well as any important details about your needs.</p>
  <div class="btn" style="left:111px;top:2542px;width:163px;height:50px">Learn More <span class="dot"></span></div>
  <div class="quality-frame"></div>
  <div class="quality-photo" role="img" aria-label="Electrician testing wiring with a red multimeter probe"></div>
</section>

<section class="newsletter" role="img" aria-label="Blurred warm-toned workshop backdrop">
  <h3 class="display" style="color:#fff">SIGN UP FOR NEWSLETTER</h3>
  <p>Sed ut perspiciatis unde omnis iste natus error sit voluptatem accusantium dolor.</p>
  <div class="news-form"><span>Email Address</span><b>SUBSCRIBE</b></div>
</section>

<section class="testimonials">
  <h2 class="display">TESTIMONIALS</h2>
  <div class="quote-card" style="left:111px"><span class="flag"><i>“</i></span><p>Sed ut perspiciatis unde omnis iste natus error sit voluptatemdoloremquelaudantium, totam rem aperiam, eaque ipsa</p><div class="stars">★★★★★</div><div class="avatar" role="img" aria-label="Client portrait"></div><div class="who"><b>OWEN HARTLEY</b>Businessman</div></div>
  <div class="quote-card featured" style="left:440px"><span class="flag"><i>“</i></span><p>Sed ut perspiciatis unde omnis iste natus error sit voluptatemdoloremquelaudantium, totam rem aperiam, eaque ipsa</p><div class="stars">★★★★★</div><div class="avatar" role="img" aria-label="Client portrait"></div><div class="who"><b>OWEN HARTLEY</b>Businessman</div></div>
  <div class="quote-card" style="left:769px"><span class="flag"><i>“</i></span><p>Sed ut perspiciatis unde omnis iste natus error sit voluptatemdoloremquelaudantium, totam rem aperiam, eaque ipsa</p><div class="stars">★★★★★</div><div class="avatar" role="img" aria-label="Client portrait"></div><div class="who"><b>OWEN HARTLEY</b>Businessman</div></div>
</section>

<section class="contact">
</section>
<div class="machines" role="img" aria-label="Faint silhouettes of construction machinery"></div>
<div class="contact-panel"><small>CONTACT US</small><h3>LET'S GO<br>GOOD<br>TOGETHER</h3></div>
<div class="contact-frame"></div>
<div class="form-card">
  <h4 class="display">SEND US A MESSAGE</h4>
  <div class="field" style="left:42px;top:94px"><label>YOUR NAME</label><span>Jane Carter</span></div>
  <div class="field" style="left:296px;top:94px"><label>COMPANY</label><span>janecarter@mailbox.us</span></div>
  <div class="field" style="left:42px;top:176px"><label>EMAIL ADDRESS</label><span>janecarter@mailbox.us</span></div>
  <div class="field" style="left:296px;top:176px"><label>PHONE</label><span>1 555 000 000</span></div>
  <div class="field" style="left:42px;top:260px;width:435px"><label>MESSAGE</label><span>Hi , do you have a moment to talk about Us</span><br><br></div>
  <div class="send"><svg width="50" height="50" viewBox="0 0 50 50"><path d="M15 26 L35 16 L29 35 L25 28 Z" fill="#fff"/></svg></div>
</div>

<footer class="site-footer">
  <div class="footer-brand"><span class="mark"></span><span class="brand-name">SIR VANTELO</span></div>
  <div class="f-col" style="left:399px"><h5>Quick Links</h5><ul><li>Home</li><li>About Us</li><li>Our Services</li><li>Latest Blog</li><li>Contact Us</li></ul></div>
  <div class="f-col" style="left:570px"><h5>Our Services</h5><ul><li>FAQ</li><li>Job Opportunities</li><li>Contractor</li><li>Subcontractor Agreement</li><li>Help Service</li></ul></div>
  <div class="f-col f-contact" style="left:808px"><h5>Contact Us</h5><div style="margin-top:24px"><i></i>Address<br>Marlow Ridge, PA 17990</div><div><i></i>Tel No : +1 (555) 240-1187</div><div><i></i>Email : info@sirvantelo.us</div></div>
</footer>
<div class="footer-bottom" style="left:113px">© 2021 Sir Vantelo. All Rights Reserved</div>
<div class="footer-bottom" style="left:845px">Privacy Policy &nbsp;|&nbsp; Terms &amp; Conditions</div>

</body>
</html>
```